PuraVeln

Hi, We are looking for a design Label for our Packaged Drinking Water. We want a label in rich color. The current Label is uploaded. We wish for a much brighter color rather than black. Our current label is in black. We have attached other company labels to give you idea. The Solmira bottle image is also uploaded they use sticker for their bottle, front sticker contains name and back sticker's inner portion has graphics and the outer side has information we also open to that.
Industry/Entity Type
Packaged Drinking Water Bottle Brand
Look and feel
Each slider illustrates characteristics of the customer's brand and the style your logo design should communicate.

```html
<!DOCTYPE html>
<html lang="en">
<head>
<meta charset="utf-8">
<title>PuraVeln – Packaged Drinking Water Label</title>
<link href="https://fonts.googleapis.com/css2?family=Poppins:wght@600&family=Arimo:wght@400&display=swap" rel="stylesheet">
<style>
  :root {
    --backdrop: #17324b;
    --label-white: #ffffff;
    --brand-ink: #6d72b8;
    --tagline-ink: #2c3552;
    --wave-deep: #72bf9c;
    --wave-light: #a3ddc6;
    --confetti-teal: #8fd3d0;
    --confetti-violet: #8a86c8;
    --mark-green: #1f9a4a;
  }
  html, body {
    margin: 0;
    padding: 0;
    width: 1200px;
    height: 1198px;
    overflow: hidden;
    background: var(--backdrop);
  }
  .canvas {
    position: relative;
    width: 1200px;
    height: 1198px;
  }
  .label {
    position: absolute;
    left: 100px;
    top: 221px;
    width: 1000px;
    height: 756px;
    background: var(--label-white);
    overflow: hidden;
  }
  .label-wave {
    position: absolute;
    inset: 0;
    width: 100%;
    height: 100%;
  }
  .confetti {
    position: absolute;
    border-radius: 50%;
    opacity: 0.45;
    filter: blur(18px);
  }
  .confetti--top-left {
    left: -20px;
    top: -30px;
    width: 520px;
    height: 190px;
    background: radial-gradient(ellipse at 30% 40%, var(--confetti-teal), transparent 70%);
  }
  .confetti--lower-right {
    left: 400px;
    top: 400px;
    width: 600px;
    height: 230px;
    background: radial-gradient(ellipse at 70% 50%, var(--confetti-violet), transparent 70%);
  }
  .brand-name {
    position: absolute;
    left: 0;
    right: 0;
    top: 120px;
    margin: 0;
    text-align: center;
    font-family: "Poppins", sans-serif;
    font-weight: 600;
    font-size: 168px;
    line-height: 1.2;
    letter-spacing: 2px;
    color: var(--brand-ink);
  }
  .brand-name .trademark {
    font-size: 24px;
    vertical-align: 112px;
    margin-left: 6px;
  }
  .tagline {
    position: absolute;
    left: 0;
    right: 0;
    top: 405px;
    margin: 0;
    text-align: center;
    font-family: "Arimo", sans-serif;
    font-size: 37px;
    color: var(--tagline-ink);
    letter-spacing: 0.5px;
  }
  .diet-mark {
    position: absolute;
    left: 792px;
    top: 632px;
    width: 48px;
    height: 48px;
    box-sizing: border-box;
    border: 4px solid var(--mark-green);
    background: var(--label-white);
  }
</style>
</head>
<body>
  <main class="canvas">
    <section class="label">
      <svg class="label-wave" viewBox="0 0 1000 756" preserveAspectRatio="none" aria-hidden="true">
        <defs>
          <linearGradient id="waveFill" x1="0" y1="0" x2="1" y2="0">
            <stop offset="0" stop-color="var(--wave-deep)"/>
            <stop offset="1" stop-color="var(--wave-light)"/>
          </linearGradient>
        </defs>
        <path d="M0,500 C160,470 300,640 460,655 C620,670 780,590 1000,572 L1000,756 L0,756 Z" fill="url(#waveFill)"/>
      </svg>
      <div class="confetti confetti--top-left" role="img" aria-label="Scattered teal and violet triangle confetti pattern"></div>
      <div class="confetti confetti--lower-right" role="img" aria-label="Scattered violet and blue triangle confetti pattern above the wave"></div>
      <h1 class="brand-name">PuraVeln<span class="trademark">™</span></h1>
      <p class="tagline">PACKAGED DRINKING WATER</p>
      <div class="diet-mark" aria-hidden="true"></div>
    </section>
  </main>
</body>
</html>
```